Our company is called QR horizon clinical innovatiom which based in hong kong and doing bio-medical research and production

We need a Label design for our new product Silver ion Antibacterial & Antivirus Spray.
The product features are
1. Long-lasting and long-term sterilization and anti-virus adopts ionized silver and colloidal silver technology, far exceeding the sterilization effective time of similar products on the market, and can last 7 to 20 days
2. Silver ions are harmless to human health and edible, non-volatile, can contact human skin and mouth, and the effect is far more than 75% of alcohol products and healthier than alcohol products
3. Silver ion sterilization and anti-viral spray has super anti-infection and healing effects on secondary wounds
4. Mask can be used in 7 days after one spray on it
5. can kill 99.9% bacteria and 650 species of virus
our target customers are states and europe.
6, it will come with some flavour into the product , lemon, apple , peach, lavanter and variety purfumes smells ,

the label design should have elements of
our colurs combinations navy blu-orange, anti-covid19 .

here comes with the old design and products
and the competitors design

Target Market(s)

europe and united states

Industry/Entity Type

Health Care

Logo Text

QR HORIZON CLINICAL OR QR CLIN-WORKS

Colors
3277b5
f37122

Requirements
Must have
• 1. the product specifications and details must be included just like the old one.
2.nano colloidal silver ion technology is used
3. must be emphasis the product is long acting for 7days +
4. anti virus and anti bacteriel need to be seen very well
oral cleaning , on mask on shirt on everything, surface and environmnet deinfection
Nice to have
• livible attractive design that sell itself
its not medicine but work for health

```html
<!DOCTYPE html>
<html lang="en">
<head>
<meta charset="utf-8">
<title>QR CLIN-WORKS Silver Ion Antibacterial &amp; Antivirus Spray Label</title>
<link href="https://fonts.googleapis.com/css2?family=Michroma&family=Nunito:wght@400;700;800;900&family=Oswald:wght@500&display=swap" rel="stylesheet">
<style>
  :root {
    --navy: #0f4a8a;
    --blue: #3277b5;
    --blue-light: #5a9fd6;
    --orange: #f37122;
    --orange-deep: #e05a12;
    --green: #7ed321;
    --white: #ffffff;
    --silver-light: #f2f4f6;
    --silver-dark: #8e969e;
    --ink: #1e1e1e;
    --page: #f5f5f5;
  }
  * { margin: 0; padding: 0; box-sizing: border-box; }
  html, body { width: 1058px; height: 1200px; overflow: hidden; background: var(--page); }
  body { position: relative; font-family: "Nunito", sans-serif; }

  .label {
    position: absolute; left: 253px; top: 40px;
    width: 552px; height: 1120px;
    background: var(--white);
    overflow: hidden;
  }
  .label-shapes { position: absolute; inset: 0; }

  .brand { position: absolute; left: 10px; top: 67px; display: flex; align-items: center; gap: 12px; }
  .brand-dot { width: 70px; height: 70px; border-radius: 50%; background: var(--blue); }
  .brand-name { font-weight: 800; font-size: 20px; color: var(--blue); letter-spacing: 0.5px; }

  .claim-badge { position: absolute; left: 283px; top: 52px; width: 155px; text-align: center; color: var(--ink); }
  .claim-badge .claim-top { font-weight: 900; font-size: 17px; line-height: 1.4; }
  .claim-badge .claim-rate { font-weight: 900; font-style: italic; font-size: 32px; line-height: 1.1; }

  .virus-art {
    position: absolute; left: 0; top: 510px; width: 230px; height: 210px;
    background: radial-gradient(circle at 62% 45%, rgba(170,230,110,.95) 0 28%, rgba(95,190,60,.55) 42%, rgba(60,160,40,0) 70%);
  }

  .headline { position: absolute; left: 100px; width: 380px; text-align: center; }
  .headline-silver {
    top: 330px; font-family: "Michroma", sans-serif; font-size: 44px; letter-spacing: -1px;
    background: linear-gradient(180deg, var(--silver-light) 0 45%, var(--silver-dark) 60%, var(--silver-light) 100%);
    -webkit-background-clip: text; background-clip: text; color: transparent;
  }
  .headline-main { top: 392px; font-weight: 900; font-size: 46px; color: var(--white); letter-spacing: 0.5px; }
  .headline-virus { top: 448px; font-weight: 900; font-size: 46px; color: var(--white); }
  .headline-virus .accent { color: var(--green); }
  .headline-spray { top: 508px; left: 225px; width: auto; font-weight: 400; font-size: 37px; color: var(--white); letter-spacing: 1px; }

  .kill-claim { position: absolute; left: 236px; top: 592px; font-weight: 900; font-size: 21px; line-height: 1.45; color: var(--green); }

  .feature { position: absolute; left: 185px; color: var(--white); }
  .feature-title { font-weight: 900; font-size: 46px; line-height: 1; }
  .feature-text { margin-top: 10px; font-weight: 800; font-size: 17px; line-height: 1.5; }
  .feature-days { top: 733px; }
  .feature-silver { top: 888px; }

  .usage {
    position: absolute; top: 1020px; left: 122px;
    display: flex; gap: 6px; list-style: none;
  }
  .usage-item {
    width: 84px; text-align: center; color: var(--white);
    font-weight: 800; font-size: 10px; line-height: 1.3; white-space: nowrap;
  }
  .usage-item svg { display: block; margin: 0 auto 6px; }

  .volume {
    position: absolute; right: 0; top: 1022px; width: 68px; height: 84px;
    background: var(--orange-deep); border-radius: 14px 0 0 0;
    display: flex; align-items: center; justify-content: center;
    font-family: "Oswald", sans-serif; font-size: 24px; color: var(--white); letter-spacing: -0.5px;
  }
</style>
</head>
<body>
<main class="label">
  <svg class="label-shapes" viewBox="0 0 552 1120" width="552" height="1120" aria-hidden="true">
    <defs>
      <linearGradient id="blueField" x1="0" y1="0" x2="1" y2="0">
        <stop offset="0" stop-color="#6fb0e0"/>
        <stop offset="0.45" stop-color="#3277b5"/>
        <stop offset="1" stop-color="#0f4a8a"/>
      </linearGradient>
      <linearGradient id="orangeField" x1="0" y1="0" x2="1" y2="1">
        <stop offset="0" stop-color="#f48a45"/>
        <stop offset="1" stop-color="#e05a12"/>
      </linearGradient>
      <linearGradient id="silverTab" x1="0" y1="0" x2="1" y2="0">
        <stop offset="0" stop-color="#9aa2aa"/>
        <stop offset="0.5" stop-color="#f4f6f8"/>
        <stop offset="1" stop-color="#9aa2aa"/>
      </linearGradient>
    </defs>
    <polygon class="band-orange" points="0,198 270,116 270,38 552,28 552,1105 0,1105" fill="url(#orangeField)"/>
    <polygon class="band-white" points="66,1105 66,262 552,95 552,1105" fill="#ffffff"/>
    <path class="field-blue" d="M90,1105 V270 Q90,250 110,244 L552,110 V1105 Z" fill="url(#blueField)"/>

    <circle cx="120" cy="790" r="50" fill="var(--orange)"/>
    <circle cx="120" cy="790" r="36" fill="none" stroke="#ffffff" stroke-width="3"/>
    <g fill="none" stroke="#ffffff" stroke-width="3">
      <rect x="104" y="772" width="32" height="34" rx="4"/>
      <line x1="104" y1="782" x2="136" y2="782"/>
    </g>
    <text x="120" y="802" text-anchor="middle" fill="#ffffff" font-family="Nunito, sans-serif" font-weight="900" font-size="18">7</text>

    <circle cx="120" cy="945" r="50" fill="var(--orange)"/>
    <circle cx="120" cy="945" r="36" fill="none" stroke="#ffffff" stroke-width="3"/>
    <g fill="none" stroke="#ffffff" stroke-width="2.5">
      <polygon points="120,928 135,937 135,953 120,962 105,953 105,937"/>
      <circle cx="120" cy="928" r="4" fill="var(--orange)"/>
      <circle cx="135" cy="937" r="4" fill="var(--orange)"/>
      <circle cx="135" cy="953" r="4" fill="var(--orange)"/>
      <circle cx="120" cy="962" r="4" fill="var(--orange)"/>
      <circle cx="105" cy="953" r="4" fill="var(--orange)"/>
      <circle cx="105" cy="937" r="4" fill="var(--orange)"/>
    </g>

    <path d="M277,30 H444 V230 A83.5,83.5 0 0 1 277,230 Z" fill="var(--navy)" opacity="0.85"/>
    <path d="M283,35 H438 V228 A77.5,77.5 0 0 1 283,228 Z" fill="url(#silverTab)"/>
    <circle cx="360" cy="232" r="46" fill="none" stroke="#2a2a2a" stroke-width="3"/>
    <circle cx="360" cy="232" r="38" fill="none" stroke="#2a2a2a" stroke-width="6"/>
    <g stroke="#2a2a2a" stroke-width="3" stroke-linecap="round">
      <circle cx="360" cy="232" r="15" fill="#2a2a2a"/>
      <line x1="360" y1="212" x2="360" y2="252"/>
      <line x1="340" y1="232" x2="380" y2="232"/>
      <line x1="346" y1="218" x2="374" y2="246"/>
      <line x1="374" y1="218" x2="346" y2="246"/>
      <line x1="333" y1="205" x2="387" y2="259" stroke-width="6"/>
    </g>
  </svg>

  <div class="brand">
    <span class="brand-dot"></span>
    <span class="brand-name">QR CLIN-WORKS</span>
  </div>

  <div class="claim-badge">
    <p class="claim-top">KILLS VIRUS<br>&amp; BACTERIA</p>
    <p class="claim-rate">99,99%</p>
  </div>

  <div class="virus-art" role="img" aria-label="Illustration of a green virus particle dissolving into fragments"></div>

  <h1 class="headline headline-silver">SILVER ION</h1>
  <p class="headline headline-main">ANTIBACTERIAL</p>
  <p class="headline headline-virus">&amp; <span class="accent">ANTIVIRUS</span></p>
  <p class="headline headline-spray">SPRAY</p>

  <p class="kill-claim">CAN KILL 99.9% BACTERIA<br>AND 650 SPECIES OF VIRUS</p>

  <section class="feature feature-days">
    <h2 class="feature-title">7DAYS +</h2>
    <p class="feature-text">MUST BE EMPHASIS THE PRODUCT<br>IS LONG ACTING</p>
  </section>

  <section class="feature feature-silver">
    <h2 class="feature-title">SILVER ION</h2>
    <p class="feature-text">NANO COLLOIDAL SILVER ION<br>TECHNOLOGY IS USED</p>
  </section>

  <ul class="usage">
    <li class="usage-item">
      <svg width="40" height="40" viewBox="0 0 40 40"><circle cx="20" cy="20" r="18" fill="none" stroke="#fff" stroke-width="2"/><path d="M11,18 Q12,28 20,29 Q28,28 29,18" fill="none" stroke="#fff" stroke-width="2"/></svg>
      HAND<br>PROTECTION
    </li>
    <li class="usage-item">
      <svg width="40" height="40" viewBox="0 0 40 40"><circle cx="20" cy="20" r="18" fill="none" stroke="#fff" stroke-width="2"/><rect x="11" y="14" width="18" height="12" rx="4" fill="none" stroke="#fff" stroke-width="2"/><line x1="13" y1="18" x2="27" y2="18" stroke="#fff" stroke-width="1.5"/><line x1="13" y1="22" x2="27" y2="22" stroke="#fff" stroke-width="1.5"/></svg>
      FACE MASK<br>SURFACE
    </li>
    <li class="usage-item">
      <svg width="40" height="40" viewBox="0 0 40 40"><circle cx="20" cy="20" r="18" fill="none" stroke="#fff" stroke-width="2"/><rect x="11" y="20" width="6" height="9" rx="1" fill="#fff"/><circle cx="24" cy="17" r="6" fill="#fff"/></svg>
      ORAL<br>CLEANING
    </li>
    <li class="usage-item">
      <svg width="40" height="40" viewBox="0 0 40 40"><circle cx="20" cy="20" r="18" fill="none" stroke="#fff" stroke-width="2"/><circle cx="20" cy="14" r="4" fill="none" stroke="#fff" stroke-width="2"/><path d="M13,28 Q20,18 27,28" fill="none" stroke="#fff" stroke-width="2"/></svg>
      MATERNAL AND<br>CHILD SAFETY
    </li>
  </ul>

  <div class="volume">100 ML</div>
</main>
</body>
</html>
```